Muffin Loom print Advertisement

We are a new online-based store searching for an awesome print advertisement design to use in all our current and future ads. We need an ad that pops and to prompt readers to visit my website (and make a purchase).

Somewhere on the ad, I would like a small section where I can easily change out coupon codes so I can easily differentiate where our marketing effort succeed.

If you think there are any photos on our website that is better suited for the ad, please let us know and we'll post it up here for you to use!

Ad size should be 2.1875"width (656px) x 2.8"height (840px).

www.muffinloomshop.example

Target Market(s)

Female age 16 to 40.

Requirements
Must have
• Section where we can put coupon code.

```html
<!DOCTYPE html>
<html lang="en">
<head>
<meta charset="utf-8">
<title>Muffin Loom – Print Advertisement</title>
<link rel="stylesheet" href="https://fonts.googleapis.com/css2?family=Arimo:wght@700&family=Tinos:ital@1&display=swap">
<style>
  :root {
    --canvas-bg: #ffffff;
    --tag-red: #c0303c;
    --band-red: #c94650;
    --panel-fill: #f3eeef;
    --panel-line: #d4747d;
    --name-pink: #d9637a;
    --photo-left-a: #6f4a2e;
    --photo-left-b: #b9856a;
    --photo-right-a: #f3eadc;
    --photo-right-b: #d9c6ae;
    --green: #1f7a1f;
    --ink: #111111;
    --coupon-ink: #3a3a3a;
  }
  html, body {
    margin: 0;
    padding: 0;
    width: 937px;
    height: 1200px;
    overflow: hidden;
    background: var(--canvas-bg);
  }
  .ad {
    position: relative;
    width: 937px;
    height: 1200px;
    overflow: hidden;
  }
  .ad-shapes {
    position: absolute;
    inset: 0;
  }
  .brand-name {
    position: absolute;
    left: 0;
    width: 937px;
    top: 370px;
    margin: 0;
    text-align: center;
    font-family: "Arimo", Arial, sans-serif;
    font-weight: 700;
    font-size: 124px;
    line-height: 128px;
    color: var(--name-pink);
  }
  .site-url {
    position: absolute;
    left: 0;
    width: 937px;
    top: 730px;
    margin: 0;
    text-align: center;
    font-family: "Arimo", Arial, sans-serif;
    font-weight: 700;
    font-size: 56px;
    letter-spacing: -1px;
    color: var(--green);
  }
  .tagline {
    position: absolute;
    left: 0;
    width: 937px;
    top: 812px;
    margin: 0;
    text-align: center;
    font-family: "Tinos", "Times New Roman", serif;
    font-style: italic;
    font-size: 84px;
    line-height: 90px;
    color: var(--ink);
  }
  .call-to-action {
    position: absolute;
    left: 0;
    width: 937px;
    top: 988px;
    margin: 0;
    text-align: center;
    font-family: "Arimo", Arial, sans-serif;
    font-weight: 700;
    font-size: 58px;
    letter-spacing: -1px;
    color: var(--green);
  }
  .coupon-code {
    position: absolute;
    right: 62px;
    top: 1142px;
    margin: 0;
    font-family: "Arimo", Arial, sans-serif;
    font-weight: 700;
    font-size: 22px;
    color: var(--coupon-ink);
  }
</style>
</head>
<body>
<main class="ad">
  <svg class="ad-shapes" width="937" height="1200" viewBox="0 0 937 1200">
    <defs>
      <clipPath id="tag-clip">
        <path d="M64 26 H871 L926 157 V1188 H11 V170 Z"/>
      </clipPath>
      <linearGradient id="photo-left-tone" x1="0" y1="0" x2="1" y2="1">
        <stop offset="0" stop-color="var(--photo-left-a)"/>
        <stop offset="1" stop-color="var(--photo-left-b)"/>
      </linearGradient>
      <linearGradient id="photo-right-tone" x1="0" y1="0" x2="1" y2="1">
        <stop offset="0" stop-color="var(--photo-right-a)"/>
        <stop offset="1" stop-color="var(--photo-right-b)"/>
      </linearGradient>
    </defs>

    <g class="tag" clip-path="url(#tag-clip)">
      <rect class="tag-band" x="0" y="0" width="937" height="1200" fill="var(--band-red)"/>
      <rect class="photo-left" x="0" y="0" width="472" height="340" fill="url(#photo-left-tone)"
            role="img" aria-label="Photo of handmade gingerbread ornament being hung on a hook"/>
      <rect class="photo-right" x="472" y="0" width="465" height="340" fill="url(#photo-right-tone)"
            role="img" aria-label="Photo of assorted retro paper stickers and labels"/>
      <rect class="content-panel" x="54" y="330" width="829" height="844"
            fill="var(--panel-fill)" stroke="var(--panel-line)" stroke-width="3"/>
    </g>

    <path class="tag-border" d="M64 26 H871 L926 157 V1188 H11 V170 Z"
          fill="none" stroke="var(--tag-red)" stroke-width="8" stroke-linejoin="round"/>
  </svg>

  <h1 class="brand-name">Muffin<br>Loom</h1>
  <p class="site-url">www.muffinloomshop.example</p>
  <p class="tagline">Modern Crafts<br>&amp; Accessories</p>
  <p class="call-to-action">Order up some Fun Today!</p>
  <p class="coupon-code">Coupon Code</p>
</main>
</body>
</html>
```